Jewelers Website

This is for the DESIGN ONLY.
I am a software programmer and will be doing the development.
New website design for
www.lumaoakstones.com.au
Need a fresh new look for an online only jewellery business who produce their jewellery by hand. I would like it designed in a parallax style. Feel free to recommend fonts to use for the site. This is an Australian based company located in NSW so shots of sites in NSW might make nice background images.
http://brixolatemplates.net/demo/#theme=parallax
To contain the below sections
About Us
Contact Us
Gallery
Testimonials
Diamond Types
The colour scheme is to be Black / White and Silver.
With the Parallax style there will be moving sections and images for added impact.
Target Market(s)
Young Adults mainly engagement jewellery
Industry/Entity Type
Software
Look and feel

```html
<!DOCTYPE html>
<html lang="en">
<head>
<meta charset="utf-8">
<title>Luma Oak Stones — Handmade Jewellery</title>
<link rel="stylesheet" href="https://fonts.googleapis.com/css2?family=Roboto:ital,wght@0,300;0,400;0,500;1,400&display=swap">
<style>
:root{
  --black:#000;
  --ink:#0b0b0c;
  --charcoal:#1a1a1a;
  --panel:#2b2b2b;
  --nav:#161616;
  --nav-active:#262626;
  --silver:#bdbdbd;
  --muted:#7d7d7d;
  --white:#fff;
  --line:rgba(255,255,255,.6);
}
*{margin:0;padding:0;box-sizing:border-box}
html,body{width:1200px;height:2769px;overflow:hidden;background:var(--black)}
body{font-family:"Roboto",Arial,sans-serif;color:var(--white);position:relative}
section,header,nav,footer{position:absolute;left:0;width:1200px;overflow:hidden}
.abs{position:absolute}
.upper{text-transform:uppercase}
a{color:inherit;text-decoration:none}

/* hero */
.hero{top:0;height:520px;background:#0e0e0f}
.hero-photo{position:absolute;inset:0;background:
  radial-gradient(ellipse 520px 260px at 78% 22%,rgba(200,200,200,.55) 0%,rgba(120,120,120,.35) 40%,transparent 75%),
  radial-gradient(ellipse 420px 90px at 62% 74%,rgba(230,230,230,.35) 0%,transparent 70%),
  linear-gradient(180deg,transparent 76%,rgba(255,255,255,.06) 80%,transparent 84%),
  linear-gradient(180deg,#1b1b1d 0%,#2c2c2e 35%,#3a3a3c 62%,#2a2a2a 76%,#141414 88%,#070707 100%)}
.brand{left:166px;top:120px;font-weight:400;font-size:19px;line-height:22px;letter-spacing:1.5px;color:#e8e8e8}
.hero-title{left:166px;top:210px;font-size:29px;font-weight:400;letter-spacing:.3px}
.hero-text{left:166px;top:262px;width:320px;font-size:10.5px;line-height:21px;color:#e5e5e5}
.hero-btn{left:162px;top:350px;width:218px;height:45px;border:1px solid var(--line);font-size:10px;display:flex;align-items:center;justify-content:center;letter-spacing:.2px}

/* nav */
.main-nav{top:520px;height:58px;background:var(--nav)}
.main-nav a{position:absolute;top:0;height:58px;line-height:58px;font-size:10.5px;color:#cfcfcf;transform:translateX(-50%);white-space:nowrap}
.main-nav a.active{background:var(--nav-active);width:118px;text-align:center;transform:none;left:172px}

/* welcome */
.welcome{top:578px;height:222px;background:var(--black);text-align:center}
.section-title{font-size:21px;font-weight:500;letter-spacing:.2px}
.welcome .section-title{margin-top:58px}
.welcome p{width:680px;margin:22px auto 0;font-size:9.5px;line-height:21px;color:#a9a9a9}

/* about */
.about{top:800px;height:415px;background:var(--panel)}
.about-photo{left:0;top:0;width:606px;height:415px;background:
  radial-gradient(ellipse 200px 230px at 60% 42%,rgba(205,170,150,.75) 0%,rgba(150,110,90,.45) 45%,transparent 75%),
  radial-gradient(ellipse 220px 320px at 22% 60%,rgba(120,85,60,.75) 0%,rgba(70,50,38,.4) 55%,transparent 85%),
  radial-gradient(ellipse 250px 120px at 40% 8%,rgba(20,20,20,.9) 0%,transparent 80%),
  linear-gradient(90deg,#3b2c24 0%,#2a2523 55%,#1c1c1c 100%)}
.about-head{left:689px;top:50px;font-size:22px;line-height:28px;font-weight:500}
.about-head span{display:block;color:#9a9a9a;font-size:25px;font-weight:400}
.about-text{left:689px;top:128px;width:318px;font-size:9px;line-height:21px;color:#a3a3a3}
.about-text p+p{margin-top:20px}
.about-btn{left:689px;top:329px;width:129px;height:35px;border:1px solid #777;font-size:10px;color:#cfcfcf;display:flex;align-items:center;justify-content:center}

/* gallery */
.gallery{top:1215px;height:718px;background:
  radial-gradient(circle 60px at 90px 90px,rgba(70,70,75,.5),transparent),
  radial-gradient(circle 70px at 760px 40px,rgba(70,70,75,.45),transparent),
  radial-gradient(circle 80px at 1110px 255px,rgba(80,80,85,.5),transparent),
  radial-gradient(circle 70px at 95px 545px,rgba(60,60,65,.5),transparent),
  radial-gradient(circle 60px at 1045px 685px,rgba(60,60,65,.45),transparent),
  radial-gradient(ellipse at 50% 40%,#1a1a1e 0%,#08080a 75%)}
.gallery .section-title{position:absolute;top:60px;width:100%;text-align:center}
.tile{width:255px;height:244px;display:flex;align-items:center;justify-content:center}
.tile-frame{width:200px;height:80px;border:2px solid rgba(255,255,255,.55);display:flex;flex-direction:column;align-items:center;justify-content:center;font-size:16.5px;line-height:27px;text-align:center}

/* testimonials */
.testimonials{top:1933px;height:291px;background:var(--charcoal)}
.testimonials .section-title{position:absolute;top:61px;width:100%;text-align:center}
.avatar{width:110px;height:110px;border-radius:50%}
.quote-name{font-size:11px;letter-spacing:.3px}
.quote-date{font-size:9px;font-style:italic;color:#8a8a8a;margin-top:7px}
.quote-text{font-size:10px;line-height:21px;color:#777;margin-top:8px;width:275px}

/* diamond types */
.types{top:2224px;height:453px;background:
  radial-gradient(ellipse 260px 200px at 50% 8%,rgba(110,110,110,.55),transparent 80%),
  radial-gradient(ellipse 420px 260px at 50% 75%,rgba(80,80,80,.5),transparent 80%),
  linear-gradient(180deg,#202020,#141414)}
.types .section-title{position:absolute;top:66px;width:100%;text-align:center}
.types-intro{position:absolute;top:110px;width:100%;text-align:center;font-size:9.5px;line-height:22px;color:#e8e8e8}
.type{width:153px;text-align:center}
.type-box{width:153px;height:137px;background:radial-gradient(ellipse at 50% 50%,#6a6a6a 0%,#3d3d3d 55%,#222 100%);display:flex;align-items:center;justify-content:center}
.type-name{font-size:9.5px;margin-top:18px;font-weight:500}
.type-link{font-size:7px;margin-top:8px;color:#ddd}

/* footer */
.site-footer{top:2677px;height:92px;background:var(--ink)}
.footer-links{left:174px;top:27px;display:flex}
.footer-links a{font-size:8px;color:#888;margin-right:38px}
.copyright{left:174px;top:55px;font-size:8px;color:#777}
.social{top:31px;width:25px;height:25px;border-radius:50%;background:#2e2e2e}
</style>
</head>
<body>

<header class="hero">
  <div class="hero-photo" role="img" aria-label="Night photograph of a harbour arch bridge over water with a lit city skyline, in black and white"></div>
  <div class="abs brand upper">Luma Oak<br>Stones</div>
  <h1 class="abs hero-title upper">Luma Oak Stones</h1>
  <p class="abs hero-text upper">At Luma Oak Stones we are passionate about fine jewellery and gems. We feature one of a kind, original and elegant, handmade pieces...</p>
  <a class="abs hero-btn upper" href="#">Click here for more details</a>
  <svg class="abs" style="left:80px;top:200px" width="20" height="80" viewBox="0 0 20 80"><path d="M16 2 L4 40 L16 78" fill="none" stroke="#666" stroke-width="1.5"/></svg>
  <svg class="abs" style="left:1120px;top:200px" width="20" height="80" viewBox="0 0 20 80"><path d="M4 2 L16 40 L4 78" fill="none" stroke="#666" stroke-width="1.5"/></svg>
</header>

<nav class="main-nav upper">
  <a class="active" href="#">Home</a>
  <a href="#" style="left:356px">About us</a>
  <a href="#" style="left:497px">Contact us</a>
  <a href="#" style="left:635px">Gallery</a>
  <a href="#" style="left:777px">Testimonials</a>
  <a href="#" style="left:940px">Diamond types</a>
</nav>

<section class="welcome">
  <h2 class="section-title upper">Welcome to Luma Oak Stones</h2>
  <p class="upper">At Luma Oak Stones we are passionate about fine jewellery and gems. We feature one of a kind, original and elegant, handmade pieces. Luma Oak Stones handmade jewellery is crafted using exceptional quality metals, integrating designs that are innovative, creative, and unique.</p>
</section>

<section class="about">
  <div class="abs about-photo" role="img" aria-label="Fashion portrait of a model in sunglasses and a black glove, wearing drop earrings"></div>
  <h2 class="abs about-head upper">About<span>Luma Oak Stones</span></h2>
  <div class="abs about-text upper">
    <p>At Luma Oak Stones we are passionate about fine jewellery and gems. We feature one of a kind, original and elegant handmade pieces. Luma Oak Stones handmade jewellery is crafted using exceptional quality metals, integrating designs that are innovative, creative, and unique.</p>
    <p>After you have consulted with our experienced staff - our highly trained and experienced jewellers hand-make every piece of finely crafted jewellery with a level of care...</p>
  </div>
  <a class="abs about-btn upper" href="#">About more &nbsp;»</a>
</section>

<section class="gallery" aria-label="Gallery">
  <h2 class="section-title upper">Gallery</h2>
  <div class="abs tile" style="left:172px;top:121px;background:radial-gradient(ellipse at 35% 30%,#666,#4a4a4a 45%,#3a3a3a)" role="img" aria-label="Close-up of a diamond ring"><div class="tile-frame upper"><span>Diamond grading</span><span>View large</span></div></div>
  <div class="abs tile" style="left:463px;top:121px;background:radial-gradient(ellipse at 55% 25%,#555,#383838 50%,#2a2a2a)" role="img" aria-label="Diamonds on a dark surface"><div class="tile-frame upper"><span>Diamond grading</span><span>View large</span></div></div>
  <div class="abs tile" style="left:755px;top:121px;background:radial-gradient(ellipse at 60% 40%,#5a5a5a,#3e3e3e 50%,#303030)" role="img" aria-label="Scattered loose diamonds"><div class="tile-frame upper"><span>Diamond grading</span><span>View large</span></div></div>
  <div class="abs tile" style="left:172px;top:395px;background:radial-gradient(ellipse at 30% 60%,#555,#3c3c3c 50%,#2c2c2c)" role="img" aria-label="Diamond chain necklace"><div class="tile-frame upper"><span>Diamond grading</span><span>View large</span></div></div>
  <div class="abs tile" style="left:463px;top:395px;background:radial-gradient(ellipse at 50% 20%,#777,#4a4a4a 45%,#333)" role="img" aria-label="Large cut diamond"><div class="tile-frame upper"><span>Diamond grading</span><span>View large</span></div></div>
  <div class="abs tile" style="left:755px;top:395px;background:radial-gradient(ellipse at 50% 50%,#444,#2e2e2e 55%,#242424)" role="img" aria-label="Pile of small diamonds"><div class="tile-frame upper"><span>Diamond grading</span><span>View large</span></div></div>
</section>

<section class="testimonials">
  <h2 class="section-title upper">Testimonials</h2>
  <div class="abs avatar" style="left:200px;top:116px;background:radial-gradient(circle at 45% 40%,#7a6050,#3a2a22 60%,#1e1815)" role="img" aria-label="Customer portrait"></div>
  <div class="abs" style="left:338px;top:128px">
    <div class="quote-name upper">Anna Verity</div>
    <div class="quote-date">Posted on 27 march 2014</div>
    <div class="quote-text">It is a long established fact that a reader will be distracted by the readable content...</div>
  </div>
  <div class="abs avatar" style="left:637px;top:116px;background:radial-gradient(circle at 50% 45%,#8a7468,#3e3836 60%,#1c1c1e)" role="img" aria-label="Customer portrait"></div>
  <div class="abs" style="left:775px;top:128px">
    <div class="quote-name upper">Anna Verity</div>
    <div class="quote-date">Posted on 27 march 2014</div>
    <div class="quote-text">It is a long established fact that a reader will be distracted by the readable content...</div>
  </div>
  <svg class="abs" style="left:134px;top:152px" width="10" height="30" viewBox="0 0 10 30"><path d="M8 1 L2 15 L8 29" fill="none" stroke="#555" stroke-width="1.2"/></svg>
  <svg class="abs" style="left:1044px;top:152px" width="10" height="30" viewBox="0 0 10 30"><path d="M2 1 L8 15 L2 29" fill="none" stroke="#555" stroke-width="1.2"/></svg>
</section>

<section class="types" aria-label="Diamond types, over a faint portrait of a model">
  <h2 class="section-title upper">Diamond types</h2>
  <p class="types-intro upper">At Luma Oak Stones we specialise in creating beautiful jewellery and diamond engagement rings using the very best diamonds, gemstones and<br>precious metals from Australia and around the world.</p>
  <svg width="0" height="0" style="position:absolute"><defs>
    <radialGradient id="gem" cx="40%" cy="35%" r="70%"><stop offset="0" stop-color="#fff"/><stop offset=".45" stop-color="#d6dde6"/><stop offset="1" stop-color="#7f8a97"/></radialGradient>
  </defs></svg>
  <div class="abs type" style="left:166px;top:192px"><div class="type-box"><svg width="64" height="64" viewBox="0 0 64 64" role="img" aria-label="Round brilliant diamond"><circle cx="32" cy="32" r="30" fill="url(#gem)" stroke="#eef2f6" stroke-width="1.5"/></svg></div><div class="type-name upper">Round brilliant</div><div class="type-link upper">[ Click here for view details ]</div></div>
  <div class="abs type" style="left:345px;top:192px"><div class="type-box"><svg width="62" height="62" viewBox="0 0 62 62" role="img" aria-label="Cushion cut diamond"><rect x="2" y="2" width="58" height="58" rx="18" fill="url(#gem)" stroke="#eef2f6" stroke-width="1.5"/></svg></div><div class="type-name upper">Cushion cut</div><div class="type-link upper">[ Click here for view details ]</div></div>
  <div class="abs type" style="left:516px;top:192px"><div class="type-box"><svg width="52" height="52" viewBox="0 0 52 52" role="img" aria-label="Princess cut diamond"><rect x="2" y="2" width="48" height="48" fill="url(#gem)" stroke="#eef2f6" stroke-width="1.5"/></svg></div><div class="type-name upper">Princess</div><div class="type-link upper">[ Click here for view details ]</div></div>
  <div class="abs type" style="left:694px;top:192px"><div class="type-box"><svg width="46" height="70" viewBox="0 0 46 70" role="img" aria-label="Emerald cut diamond"><path d="M9 2 H37 L44 9 V61 L37 68 H9 L2 61 V9 Z" fill="url(#gem)" stroke="#eef2f6" stroke-width="1.5"/></svg></div><div class="type-name upper">Emerald</div><div class="type-link upper">[ Click here for view details ]</div></div>
  <div class="abs type" style="left:871px;top:192px"><div class="type-box"><svg width="66" height="60" viewBox="0 0 66 60" role="img" aria-label="Heart cut diamond"><path d="M33 57 C22 47 3 36 3 19 C3 9 11 2 20 2 C26 2 30 5 33 10 C36 5 40 2 46 2 C55 2 63 9 63 19 C63 36 44 47 33 57 Z" fill="url(#gem)" stroke="#eef2f6" stroke-width="1.5"/></svg></div><div class="type-name upper">Heart</div><div class="type-link upper">[ Click here for view details ]</div></div>
</section>

<footer class="site-footer">
  <div class="abs footer-links upper">
    <a href="#">Home</a><a href="#">About us</a><a href="#">Contact us</a><a href="#">Gallery</a><a href="#">Testimonials</a><a href="#">Diamond types</a>
  </div>
  <div class="abs copyright upper">© 2014. Luma Oak Stones. All rights reserved.</div>
  <span class="abs social" style="left:884px"></span>
  <span class="abs social" style="left:921px"></span>
  <span class="abs social" style="left:959px"></span>
  <span class="abs social" style="left:997px"></span>
</footer>

</body>
</html>
```